New, clean letterhead for law firm in Colorado using recently designed logo.

Professional letterhead for established law firm rebranding. We service high end clientele with mostly family law and personal injury cases. Need source files for future changes. Prefer logo at top, names of members and staff in left margin, contact info in footer.

Target Market(s)

High wealth individuals

Contact Information for Business Card

Need options for traditional and square two sided business cards

Font styles to use
Serif

Colors
0555a3

Requirements
Must have
• Our logo; blue, gray, and white; modern feel.
Should not have
• Images of people

```html
<!DOCTYPE html>
<html lang="en">
<head>
<meta charset="utf-8">
<title>Halvorsen Reed Law – Square Business Card</title>
<link href="https://fonts.googleapis.com/css2?family=Manrope:wght@400;500;600&display=swap" rel="stylesheet">
<style>
  :root {
    --backdrop: #9a9c9d;
    --brand-blue: #1f5fa6;
    --paper: #f4f4f3;
    --ink-gray: #8a8c8e;
    --rule-white: rgba(255,255,255,0.85);
  }
  * { margin: 0; padding: 0; box-sizing: border-box; }
  html, body {
    width: 1200px; height: 900px; overflow: hidden;
    background: var(--backdrop);
    font-family: "Manrope", Arial, sans-serif;
  }
  .card-set {
    width: 1200px; height: 900px;
    display: flex; align-items: center; justify-content: center; gap: 64px;
  }
  .card {
    width: 460px; height: 460px; position: relative;
    box-shadow: 0 12px 30px rgba(0,0,0,0.22);
  }
  .card--front {
    background: var(--brand-blue);
    display: flex; align-items: center; justify-content: center;
  }
  .wordmark {
    display: flex; flex-direction: column; align-items: center; gap: 10px;
    color: #fff; text-transform: uppercase; font-weight: 500;
  }
  .wordmark__mark {
    width: 18px; height: 18px; border-radius: 50%; background: #fff; margin-bottom: 8px;
  }
  .wordmark__name { font-size: 30px; letter-spacing: 3px; }
  .wordmark__sub { font-size: 18px; letter-spacing: 3px; }
  .card--back { background: var(--paper); }
  .card__band { height: 20px; background: var(--brand-blue); }
  .card__body { padding: 68px 56px 0; }
  .person__name {
    color: var(--brand-blue); font-size: 27px; font-weight: 500;
    text-transform: uppercase; letter-spacing: 0.5px;
  }
  .person__role { color: var(--ink-gray); font-size: 20px; margin-top: 8px; }
  .divider { width: 46px; height: 2px; background: var(--brand-blue); margin: 40px 0 28px; }
  .contact { list-style: none; }
  .contact__item { display: flex; gap: 14px; font-size: 18px; color: var(--ink-gray); line-height: 32px; }
  .contact__label { width: 18px; color: var(--brand-blue); font-weight: 600; }
  .address { margin-top: 26px; color: var(--ink-gray); font-size: 18px; line-height: 30px; }
</style>
</head>
<body>
  <main class="card-set">
    <section class="card card--front" aria-label="Card front">
      <div class="wordmark">
        <span class="wordmark__mark"></span>
        <span class="wordmark__name">Halvorsen Reed</span>
        <span class="wordmark__sub">Law, LLC</span>
      </div>
    </section>
    <section class="card card--back" aria-label="Card back">
      <div class="card__band"></div>
      <div class="card__body">
        <h1 class="person__name">Marisa Calloway</h1>
        <p class="person__role">Advocate</p>
        <div class="divider"></div>
        <ul class="contact">
          <li class="contact__item"><span class="contact__label">T</span>1300 482 915</li>
          <li class="contact__item"><span class="contact__label">M</span>(303) 55 418 62 90</li>
          <li class="contact__item"><span class="contact__label">E</span>name@halvorsen-reed.com</li>
        </ul>
        <p class="address">870 Aspen Ridge Court 4B<br>Golden, CO 80401</p>
      </div>
    </section>
  </main>
</body>
</html>
```